Bref créative
Fun, professional business cards/advertisment for dog boarding kennel
Bright Meadow Dog Boarding
I need double sided standard sized Business Card [3.5" x 2"]
Papyrus (name) and cambria (other type)
Bright & Fun-filled
Renata & Gideon - Certified Dog Lovers
481 Palomar Lane
Yellowknife, NT
brightmeadow@pawmail.example
http://www.brightmeadowdogboarding.example
Daily, weekly, monthly dog boarding.
Multi-dog discounts
Doggie day camp and overnight boarding
Individualized care, affordable rates
Formally Furlough Pet Camp & Boarding
Call to schedule services today!
On the back of the business cards we would like it quite simple- just the logo with our website and phone number
We would like the front to be able to be used as an advertisement....like made into a magnet, so on the front we would like our name, logo and small bullet points as noted in the other comments.
We would like a fun, happy, but simple appearance. Please keep the fonts the same as in the logo.
fonts to use
AI file of our logo as requested

```html
<!DOCTYPE html>
<html lang="en">
<head>
<meta charset="utf-8">
<title>Bright Meadow Dog Boarding – Stationery Set</title>
<link href="https://fonts.googleapis.com/css2?family=Caladea:wght@400;700&display=swap" rel="stylesheet">
<style>
  :root{
    --stage:#2d2e30;
    --paper:#ffffff;
    --blue:#2a78b8;
    --blue-dark:#1f5f96;
    --blue-faint:#dce9f4;
    --red:#d8453b;
    --ink:#3b4652;
    --rule:#c9d3dc;
  }
  *{box-sizing:border-box;margin:0;padding:0}
  html,body{width:1200px;height:821px;overflow:hidden}
  body{background:var(--stage);font-family:"Caladea",Georgia,serif;color:var(--ink);position:relative}
  .piece{position:absolute;background:var(--paper);overflow:hidden;box-shadow:0 4px 14px rgba(0,0,0,.35)}
  .band{position:absolute;left:0;right:0;bottom:0;background:var(--blue);color:#fff;display:flex;align-items:center;justify-content:center;text-align:center}
  .brand{display:flex;align-items:center;gap:6px;color:var(--blue);font-weight:700;line-height:1.05}
  .brand .dot{flex:none;border-radius:50%;background:var(--blue)}
  .brand.center{justify-content:center;flex-direction:column;text-align:center;gap:4px}
  .tiny{font-size:6px;line-height:1.45}

  /* business cards */
  .card{width:230px;height:132px;border-radius:6px}
  .card-front{left:40px;top:40px}
  .card-front .brand{position:absolute;left:12px;top:12px;font-size:13px}
  .card-front .brand .dot{width:16px;height:16px}
  .card-front .services{position:absolute;left:14px;top:42px;font-size:7.5px;line-height:1.5;list-style:none}
  .card-front .services li::before{content:"";display:inline-block;width:4px;height:4px;border-radius:50%;background:var(--red);margin-right:5px;vertical-align:middle}
  .card-front .band{height:22px;font-size:7px}
  .card-back{left:290px;top:40px;background:var(--blue);color:#fff;display:flex;flex-direction:column;align-items:center;justify-content:center;gap:6px}
  .card-back .brand{color:#fff;font-size:14px}
  .card-back .brand .dot{width:18px;height:18px;background:#fff}
  .card-back p{font-size:7.5px;text-align:center}

  /* folder */
  .folder{left:40px;top:200px;width:480px;height:440px;background:none;box-shadow:none;display:flex;gap:0}
  .folder-panel{position:relative;width:240px;height:100%;overflow:hidden;box-shadow:0 4px 14px rgba(0,0,0,.35)}
  .folder-cover{background:var(--paper)}
  .folder-cover .brand{position:absolute;top:70px;left:0;right:0;font-size:20px}
  .folder-cover .brand .dot{width:34px;height:34px}
  .folder-cover .wave{position:absolute;left:0;bottom:0;width:240px;height:120px}
  .folder-inner{background:var(--blue)}
  .folder-inner .mark-faint{position:absolute;top:120px;left:0;right:0;text-align:center;color:var(--blue-dark);font-weight:700;font-size:22px;line-height:1.1;opacity:.55}

  /* sheets */
  .sheet{top:40px;width:185px;height:262px}
  .letterhead{left:560px}
  .invoice{left:767px}
  .continuation{left:975px}
  .sheet .brand{position:absolute;top:14px;left:0;right:0;font-size:10px}
  .sheet .brand .dot{width:16px;height:16px}
  .sheet .band{height:18px;font-size:5.5px;padding:0 6px}
  .invoice h2{position:absolute;top:58px;right:14px;font-size:11px;color:var(--blue);letter-spacing:1px}
  .invoice .meta{position:absolute;top:60px;left:14px}
  .invoice table{position:absolute;top:88px;left:14px;width:157px;border-collapse:collapse;font-size:5.5px}
  .invoice th{background:var(--blue);color:#fff;text-align:left;padding:2px 3px;font-weight:700}
  .invoice td{border-bottom:1px solid var(--rule);height:10px;padding:0 3px}
  .invoice .totals{position:absolute;top:196px;right:14px;text-align:right}
  .invoice .thanks{position:absolute;top:222px;left:0;right:0;text-align:center;color:var(--blue);font-size:6.5px}
  .continuation .mark-faint{position:absolute;top:110px;left:0;right:0;text-align:center;color:var(--blue-faint);font-weight:700;font-size:18px;line-height:1.1}

  /* envelopes */
  .envelope{top:340px;width:290px;height:170px}
  .envelope-front{left:560px}
  .envelope-front .brand{position:absolute;left:14px;top:14px;font-size:10px}
  .envelope-front .brand .dot{width:16px;height:16px}
  .envelope-front .return{position:absolute;left:36px;top:40px}
  .envelope-front .band{height:14px}
  .envelope-back{left:870px}
  .envelope-back .flap{position:absolute;inset:0}
  .envelope-back .brand{position:absolute;left:0;right:0;top:98px;font-size:9px}
  .envelope-back .brand .dot{width:12px;height:12px}

  /* compliment slips */
  .slip{top:560px;width:290px;height:140px}
  .slip-one{left:560px}
  .slip-two{left:870px}
  .slip .brand{position:absolute;left:14px;top:16px;font-size:12px;width:120px}
  .slip .brand .dot{width:22px;height:22px}
  .slip .names{position:absolute;right:14px;top:18px;text-align:right;color:var(--blue);font-weight:700;font-size:9px;letter-spacing:.5px}
  .slip .names span{display:block;font-weight:400;font-size:6px;color:var(--ink);letter-spacing:0}
  .slip .contact{position:absolute;right:14px;top:46px;text-align:right}
  .slip .band{height:24px;font-size:6px}
</style>
</head>
<body>

  <!-- business card: front -->
  <section class="piece card card-front">
    <div class="brand"><span class="dot"></span><span>Bright Meadow<br>Dog Boarding</span></div>
    <ul class="services">
      <li>Daily, weekly, monthly dog boarding</li>
      <li>Multi-dog discounts</li>
      <li>Doggie day camp and overnight boarding</li>
      <li>Individualized care, affordable rates</li>
    </ul>
    <div class="band">Call to schedule services today! · (867) 555-0142</div>
  </section>

  <!-- business card: back -->
  <section class="piece card card-back">
    <div class="brand center"><span class="dot"></span><span>Bright Meadow Dog Boarding</span></div>
    <p>http://www.brightmeadowdogboarding.example<br>(867) 555-0142</p>
  </section>

  <!-- presentation folder -->
  <section class="piece folder">
    <div class="folder-panel folder-cover">
      <div class="brand center"><span class="dot"></span><span>Bright Meadow<br>Dog Boarding</span></div>
      <svg class="wave" viewBox="0 0 240 120" aria-hidden="true">
        <path d="M0 40 C60 10 150 70 240 30 L240 120 L0 120 Z" fill="var(--blue)"/>
      </svg>
    </div>
    <div class="folder-panel folder-inner">
      <div class="mark-faint">Bright Meadow<br>Dog Boarding</div>
    </div>
  </section>

  <!-- letterhead -->
  <section class="piece sheet letterhead">
    <div class="brand center"><span class="dot"></span><span>Bright Meadow Dog Boarding</span></div>
    <div class="band">481 Palomar Lane, Yellowknife, NT · brightmeadow@pawmail.example</div>
  </section>

  <!-- invoice -->
  <section class="piece sheet invoice">
    <div class="brand center"><span class="dot"></span><span>Bright Meadow Dog Boarding</span></div>
    <div class="meta tiny">Date:<br>Invoice No:<br>Bill To:</div>
    <h2>INVOICE</h2>
    <table>
      <thead><tr><th>Description</th><th>Qty</th><th>Price</th><th>Total</th></tr></thead>
      <tbody>
        <tr><td></td><td></td><td></td><td></td></tr>
        <tr><td></td><td></td><td></td><td></td></tr>
        <tr><td></td><td></td><td></td><td></td></tr>
        <tr><td></td><td></td><td></td><td></td></tr>
        <tr><td></td><td></td><td></td><td></td></tr>
        <tr><td></td><td></td><td></td><td></td></tr>
        <tr><td></td><td></td><td></td><td></td></tr>
      </tbody>
    </table>
    <div class="totals tiny">Subtotal<br><strong>Total</strong></div>
    <p class="thanks">Thank you for your business</p>
    <div class="band">481 Palomar Lane, Yellowknife, NT · brightmeadow@pawmail.example</div>
  </section>

  <!-- continuation sheet -->
  <section class="piece sheet continuation">
    <div class="brand center"><span class="dot"></span><span>Bright Meadow Dog Boarding</span></div>
    <div class="mark-faint">Bright Meadow<br>Dog Boarding</div>
    <div class="band">http://www.brightmeadowdogboarding.example</div>
  </section>

  <!-- envelope: front -->
  <section class="piece envelope envelope-front">
    <div class="brand"><span class="dot"></span><span>Bright Meadow Dog Boarding</span></div>
    <p class="return tiny">481 Palomar Lane<br>Yellowknife, NT</p>
    <div class="band"></div>
  </section>

  <!-- envelope: back -->
  <section class="piece envelope envelope-back">
    <svg class="flap" viewBox="0 0 290 170" aria-hidden="true">
      <path d="M0 0 L145 82 L290 0" fill="none" stroke="var(--rule)" stroke-width="1.2"/>
      <path d="M0 170 L118 72 M290 170 L172 72" fill="none" stroke="var(--rule)" stroke-width="1"/>
    </svg>
    <div class="brand center"><span class="dot"></span><span>Bright Meadow Dog Boarding</span></div>
  </section>

  <!-- compliment slips -->
  <section class="piece slip slip-one">
    <div class="brand"><span class="dot"></span><span>Bright Meadow Dog Boarding</span></div>
    <p class="names">RENATA &amp; GIDEON<span>Certified Dog Lovers</span></p>
    <p class="contact tiny">481 Palomar Lane, Yellowknife, NT<br>brightmeadow@pawmail.example<br>(867) 555-0142</p>
    <div class="band">http://www.brightmeadowdogboarding.example</div>
  </section>

  <section class="piece slip slip-two">
    <div class="brand"><span class="dot"></span><span>Bright Meadow Dog Boarding</span></div>
    <p class="names">RENATA &amp; GIDEON<span>Certified Dog Lovers</span></p>
    <p class="contact tiny">481 Palomar Lane, Yellowknife, NT<br>brightmeadow@pawmail.example<br>(867) 555-0142</p>
    <div class="band">Formally Furlough Pet Camp &amp; Boarding</div>
  </section>

</body>
</html>
```